Vondimel 30ml pipette jar Mental Health

Label and Box for 30ml amber jar with pipette.
Already have a sample design, that needs to be adapted and possibly improved for the new packaging.
Dark brown letters on White Label.
The jar 30ml with pipette / dropper is amber with dark cap. Please view the photo.
Please view all the files, which I am uploading.
Please provide a mock up version.
Thank you.

Target Market(s)

Upscale women 34-59

Industry/Entity Type

Nutrition, Medical

Requirements
Must have
• Conservative, Minimalistic, Luxury
Should not have
• Leaves

```html
<!DOCTYPE html>
<html lang="en">
<head>
<meta charset="utf-8">
<title>Vondimel 30ml Box Dieline</title>
<link rel="stylesheet" href="https://fonts.googleapis.com/css2?family=Montserrat:wght@700&family=Rubik:wght@400;500&family=Nunito:wght@600;800&family=Poppins:wght@300;600&display=swap">
<style>
  :root {
    --paper: #ffffff;
    --ink: #111111;
    --cut-line: #3a3a3a;
    --body-ink: #2b2b2b;
  }
  html, body {
    margin: 0;
    padding: 0;
    width: 1200px;
    height: 1200px;
    overflow: hidden;
    background: var(--paper);
  }
  .dieline { display: block; width: 1200px; height: 1200px; }
  .cut { fill: var(--paper); stroke: var(--cut-line); stroke-width: 1; }
  .brand-name { font-family: "Rubik", sans-serif; font-weight: 500; font-size: 21px; fill: var(--ink); }
  .brand-name--spine { font-size: 36px; }
  .product-name { font-family: "Montserrat", sans-serif; font-weight: 700; font-size: 62px; fill: var(--ink); }
  .strength { font-family: "Montserrat", sans-serif; font-weight: 700; font-size: 24px; fill: var(--ink); }
  .strength-rule { stroke: var(--ink); stroke-width: 1.6; }
  .claim-strong { font-family: "Nunito", sans-serif; font-weight: 800; font-size: 11.5px; fill: var(--ink); }
  .claim { font-family: "Nunito", sans-serif; font-weight: 600; font-size: 11px; fill: var(--ink); }
  .volume { font-family: "Rubik", sans-serif; font-weight: 500; font-size: 15px; fill: var(--ink); }
  .facts { font-family: "Poppins", sans-serif; font-weight: 300; font-size: 10px; fill: var(--body-ink); }
  .facts .head, .facts .em { font-weight: 600; fill: var(--ink); }
</style>
</head>
<body>
<svg class="dieline" viewBox="0 0 1200 1200" xmlns="http://www.w3.org/2000/svg">
  <g class="cut-shapes">
    <polygon class="cut" points="238,295 177,324 177,883 238,912"/>
    <rect class="cut" x="238" y="128" width="198" height="167"/>
    <path class="cut" d="M436 295 Q470 270 479 172 L591 172 Q600 270 634 295 Z"/>
    <path class="cut" d="M831 295 Q865 270 874 172 L986 172 Q995 270 1029 295 Z"/>
    <rect class="cut" x="238" y="295" width="198" height="617"/>
    <rect class="cut" x="436" y="295" width="198" height="617"/>
    <rect class="cut" x="634" y="295" width="197" height="617"/>
    <rect class="cut" x="831" y="295" width="198" height="617"/>
    <path class="cut" d="M436 912 Q470 937 479 1047 L591 1047 Q600 937 634 912 Z"/>
    <path class="cut" d="M831 912 Q865 937 874 1047 L986 1047 Q995 937 1029 912 Z"/>
    <rect class="cut" x="634" y="912" width="197" height="167"/>
  </g>

  <g class="top-panel" transform="rotate(180 337 205)">
    <text class="brand-name" x="337" y="237" text-anchor="middle">Halden Health</text>
  </g>

  <g class="front-panel">
    <text class="brand-name" x="337" y="408" text-anchor="middle">Halden Health</text>
    <text class="product-name" transform="translate(339 754) rotate(-90)" textLength="292" lengthAdjust="spacingAndGlyphs">VONDIMEL</text>
    <text class="strength" transform="translate(374 523) rotate(-90)">30mg</text>
    <line class="strength-rule" x1="366" y1="536" x2="366" y2="754"/>
    <text class="claim-strong" x="337" y="816" text-anchor="middle">Doctor Formulated</text>
    <text class="claim" x="337" y="830" text-anchor="middle">Developed in Clinical Practice</text>
    <text class="volume" x="337" y="873" text-anchor="middle">30ml</text>
  </g>

  <g class="spine-panel">
    <text class="brand-name brand-name--spine" transform="translate(548 716) rotate(-90)">Halden Health</text>
  </g>

  <g class="front-panel">
    <text class="brand-name" x="732" y="408" text-anchor="middle">Halden Health</text>
    <text class="product-name" transform="translate(734 754) rotate(-90)" textLength="292" lengthAdjust="spacingAndGlyphs">VONDIMEL</text>
    <text class="strength" transform="translate(769 523) rotate(-90)">30mg</text>
    <line class="strength-rule" x1="761" y1="536" x2="761" y2="754"/>
    <text class="claim-strong" x="732" y="816" text-anchor="middle">Doctor Formulated</text>
    <text class="claim" x="732" y="830" text-anchor="middle">Developed in Clinical Practice</text>
    <text class="volume" x="732" y="873" text-anchor="middle">30ml</text>
  </g>

  <text class="facts" x="853">
    <tspan class="head" x="853" y="339">Product Facts</tspan>
    <tspan x="853" y="351">Serving Size: 1 pipette / 20 drops</tspan>
    <tspan x="853" y="363">Servings per Container: 30</tspan>
    <tspan class="head" x="853" y="388">Active Formula: 30mg</tspan>
    <tspan class="em" x="853" y="400">Cannabidiol 25mg,</tspan>
    <tspan x="853" y="412"><tspan class="em">Lithium 5mg,</tspan> Pyridoxine,</tspan>
    <tspan x="853" y="424">Cobalamin, Folic Acid,</tspan>
    <tspan x="853" y="436">Cannabidiol, Aroma Lemon,</tspan>
    <tspan x="853" y="448">Aroma Orange, Hemp oil,</tspan>
    <tspan x="853" y="460">Lithium Orotate.</tspan>
    <tspan class="head" x="853" y="484">Directions:</tspan>
    <tspan x="853" y="496">Shake well to mix ingredients</tspan>
    <tspan x="853" y="508">before use. Take one pipette</tspan>
    <tspan x="853" y="520">or more after meals.</tspan>
    <tspan x="853" y="532">Adjust daily dose to your needs.</tspan>
    <tspan x="853" y="544">Do not exceed four</tspan>
    <tspan x="853" y="556">pipettes per day.</tspan>
    <tspan class="head" x="853" y="581">Directions EU only:</tspan>
    <tspan x="853" y="593">Apply content to clean dry skin.</tspan>
    <tspan x="853" y="605">For external use.</tspan>
    <tspan x="853" y="617">For best results visit</tspan>
    <tspan class="head" x="853" y="629">www.haldenhealth.com</tspan>
    <tspan class="head" x="853" y="654">Warning:</tspan>
    <tspan x="853" y="666">Not to be used by children</tspan>
    <tspan x="853" y="678">under 18 years, women who are</tspan>
    <tspan x="853" y="690">pregnant or breastfeeding.</tspan>
    <tspan x="853" y="714">Formulated by</tspan>
    <tspan class="head" x="853" y="726">Halden Health, LLC</tspan>
    <tspan x="853" y="738">Fort Collins, Colorado</tspan>
    <tspan x="853" y="750">USA</tspan>
    <tspan x="853" y="775">EU Distribution by</tspan>
    <tspan x="853" y="787"><tspan class="em">Verdan Labs</tspan>, Eood</tspan>
    <tspan x="853" y="799">18 Ivan Vazov St.</tspan>
    <tspan x="853" y="811">Sofia, Bulgaria</tspan>
    <tspan x="853" y="823">Ph. 359-812345670</tspan>
    <tspan class="head" x="853" y="848">Made in EU</tspan>
    <tspan class="head" x="853" y="872">Exp. 10.2025</tspan>
  </text>

  <g class="bottom-panel">
    <text class="brand-name" x="734" y="1031" text-anchor="middle">Halden Health</text>
  </g>
</svg>
</body>
</html>
```